New one page Homepage with registration and log in form

Hi designers!

We need a new homepage and made a skitch of how it should be.

Can you give some of your design ideas and work it out so that it actually looks great?

Its just one page, for convertion reasons.

The logo doesnt have to be changed.

It would be cool to center the logo but not sure how design technically correct that is.

The social icons can be left out.

If you could give a few mockups than we can choose the best one.

I added one screenshot sketch of the homepage.

And 2 screenshots of what the system looks like on the inside, just so you get an idea.

Thanks

Target Market(s)

Vacation rental owners who want to increase their bookings by connecting with other VR owners and managers, or by having their own booking team for a small fee.

Industry/Entity Type

Social

Number of Pages Required

1 page

Requirements
Must have
• Use your imagination please
Nice to have
• Use your imagination
• It will be a one page design so we need to impress :)
• Keep it compact, maybe a web 3.0 flat design, etc
Should not have
• Other pages.

```html
<!DOCTYPE html>
<html lang="en">
<head>
<meta charset="utf-8">
<title>Tripnook — The First Social Booking Network</title>
<link href="https://fonts.googleapis.com/css2?family=Open+Sans:wght@400;600;700&display=swap" rel="stylesheet">
<style>
:root{
  --blue:#1d4fa8;
  --blue-deep:#1446a0;
  --blue-dark:#0e3a86;
  --blue-band:#2656ad;
  --blue-faint:#3b68b8;
  --orange:#f26522;
  --white:#ffffff;
  --ink:#2b2b2b;
  --muted:#8a8f99;
  --line:#d6d9de;
  --sky-top:#8fb3d9;
  --sky-bottom:#e9eef5;
}
*{box-sizing:border-box;margin:0;padding:0}
html,body{width:761px;height:1200px;overflow:hidden}
body{font-family:"Open Sans",Arial,sans-serif;background:var(--white);color:var(--ink);position:relative}
.abs{position:absolute}

/* Hero */
.hero{position:absolute;left:0;top:0;width:761px;height:435px}
.hero-photo{position:absolute;left:0;top:0;width:761px;height:383px;
  background:linear-gradient(180deg,var(--sky-top) 0%,#c9d9ec 45%,var(--sky-bottom) 100%)}
.hero-photo .cathedral{position:absolute;left:10px;top:0;width:440px;height:383px;
  background:radial-gradient(ellipse at 45% 60%,#c0673c 0%,#8a5a3a 35%,rgba(120,140,120,.35) 65%,rgba(0,0,0,0) 80%)}
.topbar-phone{left:106px;top:4px;font-size:7px;color:var(--ink);display:flex;align-items:center;gap:5px}
.topbar-social{left:522px;top:5px;display:flex;gap:6px}
.topbar-social span{width:7px;height:7px;border-radius:50%;background:var(--blue)}
.topbar-social span.lang{margin-left:8px;background:none;border:1px solid #c33}
.brand{left:0;width:761px;top:38px;text-align:center}
.brand-name{display:inline-flex;align-items:center;gap:6px;font-weight:700;font-size:19px;color:var(--blue);letter-spacing:.5px}
.brand-name i{display:inline-block;width:12px;height:12px;background:var(--orange)}
.brand-tag{font-size:10px;color:var(--blue);font-weight:700;margin-top:2px}
.hero-band{position:absolute;left:0;top:383px;width:761px;height:52px;background:var(--blue)}
.hero-title{left:89px;top:390px;color:var(--white);font-size:18px;font-weight:600;white-space:nowrap}
.hero-sub{left:89px;top:415px;color:var(--white);font-size:9.6px;white-space:nowrap}

/* Register card */
.join-label{left:496px;top:172px;font-size:8.5px;font-weight:700;color:var(--blue)}
.reg-card{left:492px;top:196px;width:190px;height:241px;background:var(--white);box-shadow:0 2px 6px rgba(0,0,0,.25)}
.tabs{display:flex;height:23px}
.tab{flex:1;font-size:7.5px;padding:7px 12px;color:var(--ink)}
.tab.login{background:var(--orange);color:var(--white)}
.fields{padding:9px 12px 0}
.row{display:flex;gap:8px}
.field{height:20px;border:1px solid var(--line);border-radius:2px;font-size:5.5px;color:var(--muted);padding:6px 5px;margin-bottom:9px;flex:1;white-space:nowrap;overflow:hidden}
.terms{font-size:5.5px;color:var(--blue);display:flex;align-items:center;gap:6px;margin:-2px 0 6px}
.terms i{width:6px;height:6px;border:1px solid var(--line)}
.btn-register{height:20px;background:var(--orange);color:var(--white);font-size:9px;text-align:center;line-height:20px;border-radius:2px}

/* Interests slider */
.interests{position:absolute;left:0;top:435px;width:761px;height:198px;background:var(--blue-deep)}
.interest{position:absolute;top:50px;width:100px;text-align:center;color:var(--blue-faint);font-size:10px}
.interest svg{display:block;margin:0 auto 8px}
.interest.active{color:#b8cdf0}
.arrow{position:absolute;top:95px}
.dots{position:absolute;left:0;width:761px;display:flex;justify-content:center;gap:5px}
.dots span{width:9px;height:9px;border-radius:50%;border:1.5px solid var(--white)}
.dots span.on{background:var(--white)}

/* Apps */
.apps-title{left:89px;top:685px;font-size:19px;font-weight:600;color:var(--blue);line-height:23px}
.apps-sub{left:89px;top:731px;font-size:10px;color:var(--blue)}
.badges{left:74px;top:808px;display:flex;gap:4px}
.badge{width:69px;height:24px;background:#1b1b1b;border-radius:3px}
.hand-phone{left:395px;top:662px;width:240px;height:193px;
  background:radial-gradient(ellipse at 70% 45%,#f3f3f3 0%,#d9d9d9 30%,#e8c9b2 55%,rgba(255,255,255,0) 75%)}

/* Tweet band */
.tweets{position:absolute;left:0;top:855px;width:761px;height:91px;background:var(--blue-band)}
.tweet-icon{left:200px;top:22px;width:30px;height:30px;border-radius:50%;background:var(--white)}
.tweet-text{left:258px;top:22px;width:400px;font-size:6.5px;line-height:12px;color:#dfe8f7}

/* Footer */
.footer{position:absolute;left:0;top:946px;width:761px;height:234px;background:var(--blue)}
.footer-map{position:absolute;left:0;top:0;width:300px;height:234px;
  background:radial-gradient(ellipse at 45% 45%,rgba(255,255,255,.12),rgba(255,255,255,0) 70%)}
.footer-brand{left:106px;top:80px;text-align:left}
.footer-brand .brand-name{color:var(--white)}
.footer-brand .brand-tag{color:var(--white)}
.footer-about{left:298px;top:16px;width:195px;font-size:6px;line-height:10px;color:var(--white)}
.contact{left:298px;top:62px;color:var(--white);font-size:6px;line-height:20px}
.contact b{font-size:10.5px;font-weight:600;margin-left:14px}
.news-head{left:298px;top:114px;font-size:9px;color:var(--white)}
.news-copy{left:298px;top:139px;font-size:6px;font-weight:700;color:var(--white);line-height:8px}
.news-input{left:298px;top:160px;width:158px;height:15px;background:#7390c7;font-size:5.5px;color:var(--white);padding:4px 10px}
.news-btn{left:298px;top:184px;width:100px;height:17px;background:var(--orange);font-size:5.5px;color:var(--white);padding:5px 10px}
.col-head{font-size:8px;color:var(--white)}
.col-list{list-style:none;margin-top:8px}
.col-list li{font-size:5.5px;color:var(--white);line-height:9.5px}
.col-list li::before{content:"› ";}

.bottombar{position:absolute;left:0;top:1180px;width:761px;height:20px;background:var(--blue-dark);color:var(--white);font-size:6px}
.bottombar .copy{left:104px;top:6px}
.bottombar .social{left:560px;top:7px;display:flex;gap:6px}
.bottombar .social span{width:6px;height:6px;border-radius:50%;background:var(--white)}
</style>
</head>
<body>

<header class="hero">
  <div class="hero-photo" role="img" aria-label="Photograph of colourful onion-domed cathedral against a cloudy sky">
    <div class="cathedral"></div>
  </div>
  <div class="abs topbar-phone">
    <svg width="7" height="7" viewBox="0 0 10 10"><path d="M2 0l2 3-1 1c1 2 2 3 3 3l1-1 3 2-1 2C4 10 0 6 0 2z" fill="#1d4fa8"/></svg>
    1-900-555-0142
  </div>
  <div class="abs topbar-social"><span></span><span></span><span></span><span></span><span></span><span></span><span></span><span class="lang"></span></div>
  <div class="abs brand">
    <div class="brand-name"><i></i>TRIPNOOK</div>
    <div class="brand-tag">book together, host better</div>
  </div>
  <div class="hero-band"></div>
  <h1 class="abs hero-title">THE FIRST SOCIAL BOOKING NETWORK</h1>
  <p class="abs hero-sub">Join the FREE Social Booking Network with optional Personal booking team today!</p>
</header>

<div class="abs join-label">REGISTER NOW TO JOIN THE FREE BOOKING NETWORK!</div>
<form class="abs reg-card">
  <div class="tabs"><div class="tab">REGISTER</div><div class="tab login">LOGIN</div></div>
  <div class="fields">
    <div class="row"><div class="field">First Name</div><div class="field">Last Name</div></div>
    <div class="field">Username</div>
    <div class="field">Password</div>
    <div class="field">user@email.com</div>
    <div class="field">Set your contact number. Example: +12345678910</div>
    <div class="field">What your reason for joining?</div>
    <div class="terms"><i></i>I agree to the terms &amp; conditions above</div>
    <div class="btn-register">Register your account today</div>
  </div>
</form>

<section class="interests">
  <svg class="arrow" style="left:30px" width="16" height="40" viewBox="0 0 16 40"><path d="M15 1L1 20l14 19" stroke="#fff" stroke-width="1.5" fill="none"/></svg>
  <svg class="arrow" style="left:715px" width="16" height="40" viewBox="0 0 16 40"><path d="M1 1l14 19L1 39" stroke="#fff" stroke-width="1.5" fill="none"/></svg>

  <div class="interest" style="left:90px"><svg width="40" height="40" viewBox="0 0 40 40" fill="#3b68b8"><path d="M6 8h28L21 22v12h7v2H12v-2h7V22z"/><circle cx="30" cy="8" r="5"/></svg>NIGHT LIFE</div>
  <div class="interest active" style="left:183px"><svg width="44" height="40" viewBox="0 0 44 40" fill="#8fb0e6"><ellipse cx="15" cy="17" rx="12" ry="15"/><ellipse cx="29" cy="23" rx="12" ry="15" fill="#a9c2ee"/></svg>CULTURE</div>
  <div class="interest" style="left:282px"><svg width="46" height="40" viewBox="0 0 46 40" fill="#3b68b8"><circle cx="23" cy="8" r="3"/><path d="M4 30a19 19 0 0 1 38 0z"/><rect x="1" y="32" width="44" height="4"/></svg>GOURMET FOOD</div>
  <div class="interest" style="left:380px"><svg width="40" height="40" viewBox="0 0 40 40" fill="#3b68b8"><path d="M20 2l18 9H2z"/><rect x="5" y="13" width="4" height="18"/><rect x="14" y="13" width="4" height="18"/><rect x="22" y="13" width="4" height="18"/><rect x="31" y="13" width="4" height="18"/><rect x="2" y="33" width="36" height="4"/></svg>HISTORY</div>
  <div class="interest" style="left:473px"><svg width="40" height="40" viewBox="0 0 40 40" fill="#3b68b8"><path d="M19 14c-8-6-16-2-16 2 5-3 10-3 16-2zM21 14c8-6 16-2 16 2-5-3-10-3-16-2zM19 14h2l3 20h-8z"/><ellipse cx="20" cy="36" rx="14" ry="3"/></svg>BEACH</div>
  <div class="interest" style="left:566px"><svg width="40" height="40" viewBox="0 0 40 40" fill="none" stroke="#3b68b8" stroke-width="2"><path d="M10 4h20l8 10-18 22L2 14z"/><path d="M2 14h36M15 4l-3 10 8 22 8-22-3-10"/></svg>LUXURY BRAND</div>

  <div class="dots" style="top:170px"><span class="on"></span><span></span><span></span></div>
</section>

<section>
  <h2 class="abs apps-title">TAKE YOUR NETWORK ANYWHERE<br>USING THE "TRIPNOOK".</h2>
  <p class="abs apps-sub">Available on phones, tablets and desktop</p>
  <div class="abs badges"><div class="badge"></div><div class="badge"></div><div class="badge"></div><div class="badge" style="width:103px"></div></div>
  <div class="abs hand-phone" role="img" aria-label="Photograph of a hand holding a smartphone showing the app"></div>
</section>

<section class="tweets">
  <div class="abs tweet-icon"></div>
  <p class="abs tweet-text">@tripnook : Trade growth ideas with other founders. Look for ways to cross promote. Small startups<br>today may be big friends later. (9/10) 2 days ago</p>
  <div class="dots" style="top:66px"><span class="on"></span><span></span><span></span></div>
</section>

<footer class="footer">
  <div class="footer-map" role="img" aria-label="Faint world map in the background"></div>
  <div class="abs footer-brand">
    <div class="brand-name"><i></i>TRIPNOOK</div>
    <div class="brand-tag">book together, host better</div>
  </div>
  <p class="abs footer-about">Lorem ipsum dolor sit amet, consectetur adipiscing elit. Nam viverra euismod odio, gravida pellentesque urna varius vitae. Sed dui lorem, adipiscing in adipiscing et, interdum nec.</p>
  <div class="abs contact">Phone:<b>1-900-555-0142</b><br>e-mail:<b>hello@tripnook.com</b></div>
  <div class="abs news-head">NEWSLETTER SIGNUP</div>
  <div class="abs news-copy">SIGN UP FOR OUR NEWSLETTER<br>AND GET THE LATEST NEWS.</div>
  <div class="abs news-input">INSERT EMAIL</div>
  <div class="abs news-btn">SUBMIT EMAIL</div>

  <div class="abs" style="left:498px;top:18px"><div class="col-head">MENU</div>
    <ul class="col-list"><li>Appartments</li><li>Resorts</li><li>Villas</li><li>Hotels</li><li>B &amp; Bs</li><li>Guest houses</li></ul></div>
  <div class="abs" style="left:593px;top:18px"><div class="col-head">COMMUNITY</div>
    <ul class="col-list"><li>All Property types</li><li>All themes</li><li>Careers</li><li>Terms &amp; Conditions</li></ul></div>
  <div class="abs" style="left:498px;top:114px"><div class="col-head">MENU</div>
    <ul class="col-list"><li>About</li><li>Trainers</li><li>Classes</li><li>Pricing</li><li>Privacy</li><li>Contact</li></ul></div>
  <div class="abs" style="left:593px;top:114px"><div class="col-head">COMMUNITY</div>
    <ul class="col-list"><li>Blog</li><li>Forum</li><li>Support</li><li>Newsletter</li></ul></div>
</footer>

<div class="bottombar">
  <div class="abs copy">© 2014 tripnook.com</div>
  <div class="abs social"><span></span><span></span><span></span><span></span><span></span><span></span><span></span></div>
</div>

</body>
</html>
```